Professional & attention grabbing.

A business card design, front and back. I already have a logo I will attach, but I am open to something new as well.
Things to include:
Name:
Title:
Phone:
Email:
Wanting something that is professional but attention grabbing.
Also we do a lot of work using drones on natural gas pipelines (leading the future)if you want to include any of that. I'm open to ideas.
Target Market(s)
Natural gas transmission industry / greenhouse gas mitigation industry
Industry/Entity Type
Business
Contact Information for Business Card
All details have been conveyed above.
Colors
Designer to choose colors to be used in the design.
Look and feel
Each slider illustrates characteristics of the customer's brand and the style your logo design should communicate.

```html
<!DOCTYPE html>
<html lang="en">
<head>
<meta charset="utf-8">
<title>Kestrel Line Inspections – Business Card</title>
<link href="https://fonts.googleapis.com/css2?family=Didact+Gothic&display=swap" rel="stylesheet">
<style>
  :root {
    --stage: #e9e7e4;
    --card-white: #ffffff;
    --card-dark: #3a3a3b;
    --ink: #3b3b3c;
    --ink-soft: #555557;
    --accent: #c1272d;
    --rule: #e3a9ab;
    --haze: #efefef;
  }
  * { margin: 0; padding: 0; box-sizing: border-box; }
  html, body {
    width: 1200px; height: 1200px; overflow: hidden;
    background: var(--stage);
    font-family: "Didact Gothic", "Century Gothic", sans-serif;
  }
  .canvas {
    position: relative; width: 1200px; height: 1200px;
  }
  .card {
    position: absolute; left: 150px; width: 900px; height: 514px;
    border-radius: 4px;
    box-shadow: 0 10px 30px rgba(0,0,0,0.18);
    overflow: hidden;
  }
  .card--front { top: 58px; background: var(--card-white); }
  .card--back { top: 628px; background: var(--card-dark); }

  .front__haze {
    position: absolute; right: 0; top: 0; width: 520px; height: 514px;
    background: linear-gradient(100deg, rgba(239,239,239,0) 0%, var(--haze) 60%, #f6f6f6 100%);
  }

  .brand {
    display: flex; align-items: center; gap: 14px;
  }
  .brand__mark { width: 22px; height: 22px; background: var(--accent); flex: none; }
  .brand__name { font-size: 30px; color: var(--ink); letter-spacing: 0.5px; }

  .front__brand { position: absolute; left: 60px; top: 70px; }

  .person { position: absolute; left: 60px; top: 190px; }
  .person__name { font-size: 40px; color: var(--accent); line-height: 1.1; }
  .person__title { font-size: 22px; color: var(--ink-soft); margin-top: 6px; }

  .contacts { position: absolute; left: 60px; top: 318px; list-style: none; }
  .contacts li {
    display: flex; align-items: center; gap: 12px;
    font-size: 22px; color: var(--ink-soft); line-height: 1; margin-bottom: 16px;
  }
  .icon { width: 20px; height: 20px; flex: none; fill: var(--accent); }

  .divider {
    position: absolute; left: 470px; top: 318px; width: 1px; height: 110px;
    background: var(--rule);
  }
  .address { position: absolute; left: 500px; top: 318px; }
  .address__line {
    display: flex; align-items: center; gap: 12px;
    font-size: 22px; color: var(--ink-soft); line-height: 1; margin-bottom: 16px;
  }
  .address__line--indent { padding-left: 32px; }

  .back__brand {
    position: absolute; left: 50%; top: 50%; transform: translate(-50%, -50%);
  }
  .back__brand .brand__mark { background: #ffffff; width: 26px; height: 26px; }
  .back__brand .brand__name { color: #ffffff; font-size: 40px; }
</style>
</head>
<body>
<main class="canvas">

  <section class="card card--front" aria-label="Business card front">
    <div class="front__haze"></div>

    <div class="brand front__brand">
      <span class="brand__mark"></span>
      <span class="brand__name">Kestrel Line Inspections</span>
    </div>

    <div class="person">
      <p class="person__name">John Doe</p>
      <p class="person__title">Director</p>
    </div>

    <ul class="contacts">
      <li>
        <svg class="icon" viewBox="0 0 20 20" aria-hidden="true"><path d="M4 2h4l1.5 4-2.2 1.6a11 11 0 0 0 5.1 5.1L14 10.5l4 1.5v4a2 2 0 0 1-2 2A14 14 0 0 1 2 4a2 2 0 0 1 2-2z"/></svg>
        123-456-7890
      </li>
      <li>
        <svg class="icon" viewBox="0 0 20 20" aria-hidden="true"><circle cx="10" cy="10" r="8.5" fill="none" stroke="#c1272d" stroke-width="1.6"/><ellipse cx="10" cy="10" rx="3.5" ry="8.5" fill="none" stroke="#c1272d" stroke-width="1.4"/><path d="M1.5 10h17" stroke="#c1272d" stroke-width="1.4"/></svg>
        www.kestrelline.com
      </li>
      <li>
        <svg class="icon" viewBox="0 0 20 20" aria-hidden="true"><rect x="1" y="4" width="18" height="12" rx="1"/><path d="M1.5 4.5 10 11l8.5-6.5" fill="none" stroke="#fff" stroke-width="1.5"/></svg>
        jd@kestrelline.com
      </li>
    </ul>

    <div class="divider"></div>

    <div class="address">
      <p class="address__line">
        <svg class="icon" viewBox="0 0 20 20" aria-hidden="true"><path d="M10 2 1 10h3v8h4.5v-5h3v5H16v-8h3z"/></svg>
        Dummy City
      </p>
      <p class="address__line address__line--indent">Dummy country land</p>
    </div>
  </section>

  <section class="card card--back" aria-label="Business card back">
    <div class="brand back__brand">
      <span class="brand__mark"></span>
      <span class="brand__name">Kestrel Line Inspections</span>
    </div>
  </section>

</main>
</body>
</html>
```